Retiros Silencio

I want a Catholic flyer, with the Virgen Mary showing aiding, praying, and Jesus carrying the cross, to invite people to a silent retreat. The retreats are monthly. For women, they are Feb. 21, March 21, etc (every third Saturday), and for men they are Feb. 28, March 28, etc (every fourth Saturday). I want each month date to show for both women and men. Our logo should be in there, which is similar to the Holy family icon attached. Also, show that cost is $80, and the place for the retreats is Casa Alborada, 4187 Juniper Ct, Falls Church, VA and for more information to contact, for women 540-555-0147 and for men 571-555-0182. I will use the flyer for around 4 x 6 or 3 x 5 postcard. Organizers are: Nidos de Valle Claro. The flyer needs to be in spanish "RETIROS EN SILENCIO" and the months should be labeled in Spanish too.

```html
<!DOCTYPE html>
<html lang="es">
<head>
<meta charset="utf-8">
<title>Retiros en Silencio</title>
<link rel="stylesheet" href="https://fonts.googleapis.com/css2?family=Fira+Sans:wght@700;800&family=Fondamento&family=Oswald:wght@300;400;500;600;700&family=Montserrat:ital,wght@0,500;1,800&display=swap">
<style>
  :root {
    --page: #f7f8fa;
    --navy: #1b5780;
    --deep: #0c3a4c;
    --panel: #17364f;
    --red: #c0222f;
    --yellow: #fff200;
    --sky: #9ccdfa;
    --white: #ffffff;
  }
  * { margin: 0; padding: 0; box-sizing: border-box; }
  html, body { width: 837px; height: 1200px; overflow: hidden; background: var(--page); }
  .canvas { position: relative; width: 837px; height: 1200px; background: var(--page); }
  .flyer {
    position: absolute; left: 65px; top: 70px; width: 707px; height: 1061px; overflow: hidden;
    background: linear-gradient(180deg, #e7edf2 0%, #c9d7e2 28%, #8fa9be 45%, #5a84a6 62%, #2f6189 80%, #25567f 100%);
  }
  .flyer > * { position: absolute; white-space: nowrap; }
  .holy-family-art {
    left: 380px; top: 7px; width: 327px; height: 245px; border-radius: 120px 120px 20px 20px;
    background: radial-gradient(ellipse at 60% 65%, #f3d9a4 0%, #b99370 30%, #5b4c4a 65%, #2e3a4d 100%);
  }
  .mary-statue-art {
    left: 0; top: 379px; width: 188px; height: 682px; border-radius: 80px 80px 0 0;
    background: linear-gradient(90deg, #2f78c4 0%, #e9e6dc 45%, #f1ede2 60%, #2e73bd 100%);
    opacity: .95;
  }
  .title {
    left: 34px; top: 44px; z-index: 2; font-family: "Fira Sans", sans-serif; font-weight: 800;
    font-size: 71px; line-height: 84px; color: var(--navy); letter-spacing: -2px;
  }
  .invite {
    left: 30px; top: 238px; font-family: "Fondamento", cursive; font-size: 84px; line-height: 1;
    color: var(--red); text-shadow: 0 0 6px rgba(255,255,255,.8);
  }
  .headline {
    left: 122px; top: 318px; font-family: "Oswald", sans-serif; font-weight: 700; font-size: 70px;
    line-height: 1; color: var(--white); letter-spacing: -3px;
    transform: scaleX(.9); transform-origin: left top;
    text-shadow: 0 0 8px rgba(120,180,255,.7);
  }
  .monthly {
    left: 237px; top: 398px; font-family: "Montserrat", sans-serif; font-style: italic; font-weight: 800;
    font-size: 31px; line-height: 1.1; color: var(--yellow);
  }
  .venue-band { left: 321px; top: 461px; width: 386px; height: 78px; background: var(--red); }
  .pin { left: 345px; top: 479px; width: 42px; height: 42px; }
  .venue {
    left: 398px; top: 468px; font-family: "Oswald", sans-serif; font-weight: 500; font-size: 24px;
    line-height: 30px; color: var(--white);
  }
  .cost {
    left: 119px; top: 461px; width: 213px; height: 78px; background: var(--deep); border-radius: 12px;
    display: flex; align-items: center; justify-content: center; gap: 14px;
    font-family: "Oswald", sans-serif; color: var(--yellow);
  }
  .cost-label { font-weight: 500; font-size: 28px; margin-top: 14px; }
  .cost-price { font-weight: 700; font-size: 60px; line-height: 1; }
  .group { width: 290px; height: 290px; top: 577px; }
  .group-box { position: absolute; inset: 0; background: var(--panel); border-radius: 18px; opacity: .92; }
  .group-women { left: 102px; }
  .group-men { left: 414px; }
  .group-label {
    position: absolute; top: -30px; height: 65px; background: var(--sky); border-radius: 32px;
    font-family: "Oswald", sans-serif; font-weight: 600; font-size: 48px; line-height: 63px;
    color: var(--red); text-align: center; box-shadow: 0 0 14px rgba(150,205,255,.8);
  }
  .group-women .group-label { left: 23px; width: 242px; }
  .group-men .group-label { left: 47px; width: 196px; }
  .dates {
    position: absolute; left: 0; right: 0; top: 50px; text-align: center;
    font-family: "Oswald", sans-serif; font-weight: 600; font-size: 42px; line-height: 54px;
    color: var(--white); letter-spacing: -1.5px;
  }
  .dates .every { font-weight: 300; color: var(--yellow); }
  .dates .every b { font-weight: 700; }
  .dates .sat { font-weight: 300; color: var(--yellow); }
  .contact {
    width: 262px; height: 76px; top: 862px; background: var(--red); text-align: center;
    font-family: "Oswald", sans-serif; color: var(--yellow);
  }
  .contact-women { left: 115px; }
  .contact-men { left: 428px; }
  .contact-label { display: block; color: var(--white); font-size: 19px; font-weight: 400; margin-top: 4px; line-height: 24px; }
  .contact-number { display: block; font-size: 37px; font-weight: 700; line-height: 42px; }
  .organizers {
    left: 158px; top: 968px; width: 392px; display: flex; align-items: center; gap: 10px;
    font-family: "Montserrat", sans-serif; font-style: italic; font-weight: 800; font-size: 35px; color: var(--yellow);
  }
  .organizers .rule { flex: 1; height: 2px; background: var(--yellow); }
  .organizer-name {
    left: 191px; top: 1003px; font-family: "Montserrat", sans-serif; font-weight: 500; font-size: 29px;
    color: var(--white); letter-spacing: 1px;
  }
</style>
</head>
<body>
<div class="canvas">
  <main class="flyer">
    <div class="holy-family-art" role="img" aria-label="Painted Holy Family: Joseph, Mary and the Child Jesus holding a glowing light"></div>
    <div class="mary-statue-art" role="img" aria-label="Statue of the Virgin Mary in a white robe and blue mantle"></div>

    <h1 class="title">RETIROS EN<br>SILENCIO</h1>
    <p class="invite">Invite You..</p>
    <h2 class="headline">TO A SILENT RETREAT</h2>
    <p class="monthly">The Retreats are monthly</p>

    <div class="venue-band"></div>
    <svg class="pin" viewBox="0 0 42 42" aria-hidden="true">
      <circle cx="21" cy="21" r="21" fill="#0c3a4c"/>
      <path d="M21 10a8 8 0 0 0-8 8c0 6 8 14 8 14s8-8 8-14a8 8 0 0 0-8-8z" fill="#fff"/>
      <circle cx="21" cy="18" r="3" fill="#0c3a4c"/>
    </svg>
    <p class="venue">Casa Alborada, 4187<br>Juniper Ct, Falls Church, VA</p>
    <div class="cost"><span class="cost-label">COST</span><span class="cost-price">$80</span></div>

    <section class="group group-women">
      <div class="group-box"></div>
      <h3 class="group-label">For Women</h3>
      <p class="dates">February 21,<br>March 21..,<br><span class="every">(Every <b>Third</b></span><br><span class="sat">Saturday)</span></p>
    </section>
    <section class="group group-men">
      <div class="group-box"></div>
      <h3 class="group-label">For Men</h3>
      <p class="dates">February 28,<br>March 28..,<br><span class="every">(Every <b>Fourth</b></span><br><span class="sat">Saturday)</span></p>
    </section>

    <div class="contact contact-women"><span class="contact-label">CONTACT</span><span class="contact-number">540-555-0147</span></div>
    <div class="contact contact-men"><span class="contact-label">CONTACT</span><span class="contact-number">571-555-0182</span></div>

    <div class="organizers"><span class="rule"></span>Organizers<span class="rule"></span></div>
    <p class="organizer-name">Nidos de Valle Claro</p>
  </main>
</div>
</body>
</html>
```